Business Cards and Print Material
Business cards and print material
I like something that is out of the box. Something different and memorable. I will also need design for envelopes and letter heads. I like the designs so far. Please keep up the good work!
any info or ideas on what you would like ????

```html
<!DOCTYPE html>
<html lang="en">
<head>
<meta charset="utf-8">
<title>Northwind Imaging Group – Business Card</title>
<link href="https://fonts.googleapis.com/css2?family=Source+Sans+3:wght@400;600;700&display=swap" rel="stylesheet">
<style>
  :root {
    --page-bg: #ecebe8;
    --card-white: #ffffff;
    --brand-blue: #2a3f9a;
    --deep-blue: #1b2a7a;
    --bright-blue: #2c67c4;
    --text-grey: #5a5f6b;
    --rule-grey: #c9ccd3;
  }
  * { box-sizing: border-box; margin: 0; padding: 0; }
  html, body {
    width: 1200px; height: 1055px; overflow: hidden;
    background: var(--page-bg);
    font-family: "Source Sans 3", sans-serif;
  }
  .sheet {
    position: relative; width: 1200px; height: 1055px;
  }
  .card {
    position: absolute; left: 250px; width: 700px; height: 400px;
    border-radius: 22px;
    box-shadow: 0 6px 18px rgba(0,0,0,0.18);
    overflow: hidden;
  }
  .card--front { top: 95px; background: var(--card-white); }
  .card--back {
    top: 560px;
    background: radial-gradient(ellipse at 55% 70%, var(--bright-blue) 0%, var(--brand-blue) 45%, var(--deep-blue) 100%);
  }
  .brand-block {
    position: absolute; left: 40px; top: 140px; width: 290px;
    display: flex; align-items: center; gap: 12px;
  }
  .brand-dot {
    width: 18px; height: 18px; border-radius: 50%;
    background: var(--brand-blue); flex: none;
  }
  .brand-name {
    color: var(--brand-blue); font-weight: 600;
    font-size: 26px; line-height: 1.1; letter-spacing: 1px;
    text-transform: uppercase;
  }
  .divider {
    position: absolute; left: 355px; top: 45px; width: 2px; height: 250px;
    background: var(--rule-grey);
  }
  .contact {
    position: absolute; left: 380px; top: 48px; width: 300px;
    color: var(--text-grey); font-size: 15px; line-height: 1.45;
  }
  .contact__name {
    color: var(--brand-blue); font-weight: 700; font-size: 28px; line-height: 1.1;
  }
  .contact__title { font-size: 16px; margin-bottom: 24px; }
  .contact__label { color: var(--brand-blue); font-weight: 700; }
  .contact__web { color: var(--brand-blue); font-weight: 700; }
  .back-name {
    position: absolute; left: 0; right: 0; top: 185px; text-align: center;
    color: rgba(255,255,255,0.22); font-weight: 600; font-size: 22px;
    letter-spacing: 3px; text-transform: uppercase;
  }
</style>
</head>
<body>
  <main class="sheet">
    <section class="card card--front" aria-label="Business card front">
      <div class="brand-block">
        <span class="brand-dot"></span>
        <span class="brand-name">Northwind Imaging Group</span>
      </div>
      <div class="divider"></div>
      <div class="contact">
        <p class="contact__name">Tessa Wilde</p>
        <p class="contact__title">Director of Operations</p>
        <p>4410 Larkspur Way, Suite 210 <span class="contact__label">P:</span> 210.555.0187</p>
        <p>Fairhaven, TX 70512</p>
        <p><span class="contact__label">Toll Free:</span> 800.555.0142 <span class="contact__label">F:</span> 210.555.0129</p>
        <p><span class="contact__label">C:</span> 210.555.0163</p>
        <p><span class="contact__label">E:</span> tessa@northwindimaging.com</p>
        <p class="contact__web">northwindimaging.com</p>
      </div>
    </section>
    <section class="card card--back" aria-label="Business card back">
      <p class="back-name">Northwind Imaging Group</p>
    </section>
  </main>
</body>
</html>
```